Gentleman's grooming products require a business card

I need a business card that incorporates the logo [ or parts of ] that we had Art Parade design for us as uploaded.

We sell online, mens grooming products including moustache waxes, beard oils and shaving accessories.
We want a card that is classy, professional and a card that shouts mens products.

Target Market(s)

Young professional male market

Industry/Entity Type

Business

Contact Information for Business Card

Tess and Dulcie Abbott
Brass and Bristle
Purveyors of gentleman's stiffeners and grooming requisites
M :0491527306
E : tess@brassandbristle.com.au
E : dulcie@brassandbristle.com.au
E : sales@theboulevardpomade.com.au

W : www.brassandbristle.com.au

Requirements
Must have
• Class
Nice to have
• Professionalism

```html
<!DOCTYPE html>
<html lang="en">
<head>
<meta charset="utf-8">
<title>Brass and Bristle — Business Card</title>
<link rel="stylesheet" href="https://fonts.googleapis.com/css2?family=Cinzel:wght@400;600&display=swap">
<style>
  :root {
    --backdrop: #cfcfcd;
    --card: #0a0a0a;
    --ink: #f2f2f2;
    --ink-soft: #d9d9d9;
  }
  * { margin: 0; padding: 0; box-sizing: border-box; }
  html, body { width: 1200px; height: 900px; overflow: hidden; }
  body {
    background: var(--backdrop);
    font-family: "Cinzel", "Times New Roman", serif;
    color: var(--ink);
    position: relative;
  }
  .business-card {
    position: absolute;
    left: 100px; top: 164px;
    width: 1000px; height: 572px;
    background: var(--card);
    box-shadow: 0 6px 18px rgba(0,0,0,0.25);
  }
  .card-frame { position: absolute; inset: 0; }
  .brand-mark {
    position: absolute;
    left: 461px; top: 50px;
    width: 78px; height: 78px;
    border: 2px solid var(--ink);
  }
  .brand-name {
    position: absolute; left: 0; right: 0; top: 140px;
    text-align: center;
    font-size: 58px; font-weight: 400;
    letter-spacing: 1px;
    color: var(--ink);
  }
  .tagline {
    position: absolute; left: 0; right: 0; top: 240px;
    text-align: center;
    font-size: 13px; letter-spacing: 1.2px;
    color: var(--ink-soft);
  }
  .owner-names {
    position: absolute; left: 0; right: 0; top: 276px;
    text-align: center;
    font-size: 25px; font-weight: 600; letter-spacing: 1px;
  }
  .owner-role {
    position: absolute; left: 0; right: 0; top: 312px;
    text-align: center;
    font-size: 15px; letter-spacing: 1.5px;
    color: var(--ink-soft);
  }
  .contact {
    position: absolute;
    font-size: 19px; letter-spacing: 1px;
    white-space: nowrap;
  }
  .contact-email-tess { left: 60px; top: 350px; }
  .contact-mobile { left: 0; right: 0; top: 350px; text-align: center; }
  .contact-email-sales { left: 60px; top: 395px; }
  .contact-email-dulcie { right: 60px; top: 395px; }
  .contact-web { left: 0; right: 0; top: 478px; text-align: center; }
</style>
</head>
<body>
  <article class="business-card">
    <svg class="card-frame" width="1000" height="572" viewBox="0 0 1000 572" aria-hidden="true">
      <g fill="none" stroke="#f2f2f2" stroke-width="2">
        <polyline points="250,492 24,492 24,24 976,24 976,492 750,492"/>
        <line x1="230" y1="110" x2="455" y2="110"/>
        <line x1="545" y1="110" x2="770" y2="110"/>
        <line x1="230" y1="228" x2="770" y2="228"/>
      </g>
    </svg>

    <div class="brand-mark"></div>
    <h1 class="brand-name">Brass and Bristle</h1>
    <p class="tagline">PURVEYORS OF GENTLEMEN'S STIFFENERS AND GROOMING REQUISITES</p>

    <p class="owner-names">TESS AND DULCIE ABBOTT</p>
    <p class="owner-role">OWNERS</p>

    <p class="contact contact-email-tess">E : TESS@BRASSANDBRISTLE.COM.AU</p>
    <p class="contact contact-mobile">M :0491527306</p>
    <p class="contact contact-email-sales">E : SALES@THEBOULEVARDPOMADE.COM.AU</p>
    <p class="contact contact-email-dulcie">E : DULCIE@BRASSANDBRISTLE.COM.AU</p>
    <p class="contact contact-web">W : WWW.BRASSANDBRISTLE.COM.AU</p>
  </article>
</body>
</html>
```